Business Card Design Project

Looking for a cool, trendy design for new business cards for our Mobile Application business.

Quillomo Apps

www.quillomoapps.example

Target Market(s)

Looking for a bold modern design that attracts a younger demographic in the mobile space.

Industry/Entity Type

Business

Requirements
Must have
• Trendy, Easily adapted for other staff cards, works with large clients but showcases and innovative company

```html
<!DOCTYPE html>
<html lang="en">
<head>
<meta charset="utf-8">
<title>Quillomo Apps — Business Card</title>
<link rel="stylesheet" href="https://fonts.googleapis.com/css2?family=Lato:wght@300;400&display=swap">
<style>
  :root {
    --page-bg: #e9e6e1;
    --card-black: #050505;
    --card-gloss: #4a4a4d;
    --rim-light: #d9d9d9;
    --screen-light: #ffffff;
    --screen-edge: #cfcfcf;
    --ink-dark: #2e2e2e;
    --ink-soft: #a9a9a9;
  }
  html, body {
    margin: 0;
    padding: 0;
    width: 1200px;
    height: 1000px;
    overflow: hidden;
    background: var(--page-bg);
  }
  .canvas {
    position: relative;
    width: 1200px;
    height: 1000px;
  }
  .card {
    position: absolute;
    top: 372px;
    width: 530px;
    height: 255px;
  }
  .card--front { left: 50px; }
  .card--back { left: 620px; }
  .card svg {
    position: absolute;
    inset: 0;
    width: 530px;
    height: 255px;
    overflow: visible;
  }
  .screen-text {
    position: absolute;
    left: 68px;
    top: 14px;
    width: 394px;
    height: 224px;
    display: flex;
    flex-direction: column;
    align-items: center;
    justify-content: center;
    font-family: "Lato", sans-serif;
    color: var(--ink-dark);
  }
  .company-name {
    font-weight: 300;
    font-size: 25px;
    letter-spacing: 0.3px;
    margin: 0 0 6px;
  }
  .web-address {
    font-weight: 400;
    font-size: 14px;
    letter-spacing: 0.2px;
    margin: 0;
  }
  .back-name {
    position: absolute;
    left: 72px;
    top: 127px;
    transform: translate(-50%, -50%) rotate(90deg);
    font-family: "Lato", sans-serif;
    font-weight: 300;
    font-size: 13px;
    letter-spacing: 0.3px;
    color: var(--ink-soft);
    white-space: nowrap;
  }
</style>
</head>
<body>
<main class="canvas">

  <section class="card card--front" aria-label="Card front">
    <svg viewBox="0 0 530 255" aria-hidden="true">
      <defs>
        <linearGradient id="rim" x1="0" y1="0" x2="1" y2="1">
          <stop offset="0" stop-color="#777"/>
          <stop offset="0.6" stop-color="#bbb"/>
          <stop offset="1" stop-color="var(--rim-light)"/>
        </linearGradient>
        <radialGradient id="screenGlow" cx="0.5" cy="0.5" r="0.75">
          <stop offset="0" stop-color="var(--screen-light)"/>
          <stop offset="1" stop-color="var(--screen-edge)"/>
        </radialGradient>
        <linearGradient id="frontGloss" x1="0" y1="0" x2="1" y2="0">
          <stop offset="0" stop-color="#0a0a0a"/>
          <stop offset="1" stop-color="#333"/>
        </linearGradient>
      </defs>
      <g class="side-buttons" fill="#111">
        <rect x="-4" y="36" width="6" height="34" rx="2"/>
        <rect x="70" y="252" width="20" height="5" rx="1.5"/>
        <rect x="125" y="252" width="16" height="5" rx="1.5"/>
        <rect x="178" y="252" width="16" height="5" rx="1.5"/>
      </g>
      <rect class="rim" x="0" y="0" width="530" height="255" rx="28" fill="url(#rim)"/>
      <rect class="body" x="0" y="0" width="528" height="252" rx="27" fill="var(--card-black)"/>
      <polygon class="gloss" points="370,0 501,0 528,25 528,60" fill="url(#frontGloss)" opacity="0.6"/>
      <rect class="screen" x="68" y="14" width="394" height="224" fill="url(#screenGlow)"/>
      <circle class="camera" cx="22" cy="127" r="3.5" fill="#444"/>
      <rect class="speaker" x="34" y="107" width="7" height="38" rx="3.5" fill="#1a1a1a" stroke="#555" stroke-width="1"/>
      <circle class="home-button" cx="496" cy="127" r="17" fill="#101010" stroke="#2a2a2a" stroke-width="2"/>
      <rect class="home-icon" x="489" y="120" width="14" height="14" rx="2" fill="none" stroke="#aaa" stroke-width="1.3"/>
    </svg>
    <div class="screen-text">
      <p class="company-name">Quillomo Apps</p>
      <p class="web-address">www.quillomoapps.example</p>
    </div>
  </section>

  <section class="card card--back" aria-label="Card back">
    <svg viewBox="0 0 530 255" aria-hidden="true">
      <defs>
        <linearGradient id="rimBack" x1="0" y1="0" x2="1" y2="1">
          <stop offset="0" stop-color="#777"/>
          <stop offset="0.6" stop-color="#bbb"/>
          <stop offset="1" stop-color="var(--rim-light)"/>
        </linearGradient>
        <linearGradient id="backGloss" x1="0" y1="0" x2="1" y2="1">
          <stop offset="0" stop-color="var(--card-gloss)"/>
          <stop offset="1" stop-color="#2a2a2c"/>
        </linearGradient>
        <clipPath id="backShape">
          <rect x="0" y="0" width="528" height="252" rx="27"/>
        </clipPath>
      </defs>
      <g class="side-buttons" fill="#111">
        <rect x="528" y="36" width="6" height="34" rx="2"/>
        <rect x="336" y="252" width="16" height="5" rx="1.5"/>
        <rect x="389" y="252" width="16" height="5" rx="1.5"/>
        <rect x="440" y="252" width="20" height="5" rx="1.5"/>
      </g>
      <rect class="rim" x="0" y="0" width="530" height="255" rx="28" fill="url(#rimBack)"/>
      <rect class="body" x="0" y="0" width="528" height="252" rx="27" fill="var(--card-black)"/>
      <polygon class="gloss" clip-path="url(#backShape)" points="152,0 528,0 528,252 382,252" fill="url(#backGloss)"/>
    </svg>
    <div class="back-name">Quillomo Apps</div>
  </section>

</main>
</body>
</html>
```